Bref créative
MOBILE ULTRASOUND BUSINESS
Professional
Nora K. Pellway Hussel
President and Director of Ultrasound
517 Thornbury Lane #2614
Millbrook Twp. PA. 15832
nora@keystonepulsescanworks.example
keystonepulsescanworks.example
We need business cards for my husband as well, all info will be the same except for his name is Gavin P. Hussel - Chief Operating Officer for title - and gavin@keystonepulsescanworks.example
vector logo file

```html
<!DOCTYPE html>
<html lang="en">
<head>
<meta charset="utf-8">
<title>BRQMOLVEX Stationery Set</title>
<link href="https://fonts.googleapis.com/css2?family=Arimo:wght@400;700&display=swap" rel="stylesheet">
<style>
:root{
  --ink:#111214;
  --card:#0c0d0f;
  --green:#6cc04a;
  --blue:#1f7fc4;
  --blue-glow:#3aa0e8;
  --paper:#ffffff;
  --text:#333;
  --muted:#777;
  --stage:#e9e7e4;
  --rule:#bbb;
}
*{box-sizing:border-box;margin:0;padding:0}
html,body{width:1200px;height:871px;overflow:hidden}
body{background:var(--stage);font-family:"Arimo",Arial,sans-serif;color:var(--text);position:relative}
.piece{position:absolute;box-shadow:0 3px 10px rgba(0,0,0,.35)}
.brand{display:flex;align-items:center;gap:6px;white-space:nowrap}
.brand-mark{width:12px;height:12px;background:var(--green);flex:none}
.brand-name{font-weight:700;color:var(--green);letter-spacing:.04em}

/* business cards */
.card{width:194px;height:118px;background:var(--card);overflow:hidden;color:#ddd}
.card::after{content:"";position:absolute;left:0;right:0;bottom:0;height:40px;
  background:radial-gradient(ellipse at 50% 100%,var(--blue-glow),rgba(31,127,196,.3) 45%,transparent 75%)}
.card .brand{position:absolute;left:10px;top:40px}
.card .brand-name{font-size:11px}
.card-person{position:absolute;right:10px;top:10px;text-align:right;font-size:6.5px;line-height:1.4;white-space:nowrap}
.card-person strong{display:block;font-size:7.5px;color:#fff}
.card-contact{position:absolute;left:10px;bottom:10px;font-size:6px;line-height:1.45;color:#ccc;z-index:1}
.card-back .brand{left:50%;top:44px;transform:translateX(-50%)}
.card-back .brand-name{font-size:14px}
.card-back .web{position:absolute;bottom:10px;width:100%;text-align:center;font-size:6px;color:#ccc;z-index:1}

/* envelopes */
.envelope{width:522px;background:var(--paper);overflow:hidden}
.env-head{height:52px;background:var(--ink);border-bottom:4px solid var(--green);position:relative}
.env-head .brand{position:absolute;left:14px;top:18px}
.env-head .brand-name{font-size:12px}
.env-window{position:absolute;width:120px;height:36px;background:#d7d7d7;border:1px solid #bbb;border-radius:4px}
.env-return{position:absolute;left:14px;font-size:6px;line-height:1.5;color:var(--muted)}

/* letterhead */
.letterhead{width:560px;height:800px;background:var(--paper)}
.lh-band{height:64px;background:var(--ink);border-bottom:5px solid var(--green);position:relative}
.lh-band .brand{position:absolute;left:16px;top:22px}
.lh-band .brand-name{font-size:17px}
.lh-address{position:absolute;right:16px;top:12px;font-size:6.5px;line-height:1.5;color:#ccc;text-align:right}
.lh-body{padding:24px 26px;font-size:7.5px;line-height:1.6}
.lh-body p{margin-bottom:10px}
.signature{width:90px;height:20px;border-bottom:1px solid var(--text);margin:8px 0 4px}

/* fax */
.fax{width:466px;height:334px;background:var(--paper)}
.fax-head{height:92px;background:var(--ink);border-bottom:5px solid var(--green);position:relative}
.fax-head .brand{position:absolute;left:20px;top:34px}
.fax-head .brand-name{font-size:17px}
.fax-head .lh-address{top:22px}
.fax-title{position:absolute;left:150px;top:108px;font-size:16px;font-weight:700;color:var(--text)}
.fax-fields{position:absolute;left:60px;top:134px;width:380px;display:grid;grid-template-columns:1fr 1fr;gap:6px 24px;font-size:7px}
.fax-fields span{display:flex;gap:6px;border-bottom:1px solid var(--rule);padding-bottom:2px}
.fax-checks{position:absolute;left:60px;top:214px;display:flex;gap:14px;font-size:6px}
.fax-checks span::before{content:"";display:inline-block;width:6px;height:6px;border:1px solid var(--muted);margin-right:3px;vertical-align:-1px}
.fax-comments{position:absolute;left:60px;top:238px;font-size:6.5px}
</style>
</head>
<body>

<!-- business cards -->
<section class="piece card" style="left:29px;top:12px">
  <div class="brand"><span class="brand-mark"></span><span class="brand-name">BRQMOLVEX</span></div>
  <div class="card-person"><strong>Nora K. Pellway Hussel</strong>President and Director of Ultrasound</div>
  <div class="card-contact">517 Thornbury Lane #2614<br>Millbrook Twp. PA. 15832<br>Phone (555) 010-2468<br>nora@keystonepulsescanworks.example</div>
</section>
<section class="piece card card-back" style="left:233px;top:12px">
  <div class="brand"><span class="brand-mark"></span><span class="brand-name">BRQMOLVEX</span></div>
  <div class="web">keystonepulsescanworks.example</div>
</section>
<section class="piece card" style="left:29px;top:144px">
  <div class="brand"><span class="brand-mark"></span><span class="brand-name">BRQMOLVEX</span></div>
  <div class="card-person"><strong>Gavin P. Hussel</strong>Chief Operating Officer</div>
  <div class="card-contact">517 Thornbury Lane #2614<br>Millbrook Twp. PA. 15832<br>Phone (555) 010-2468<br>gavin@keystonepulsescanworks.example</div>
</section>
<section class="piece card card-back" style="left:233px;top:144px">
  <div class="brand"><span class="brand-mark"></span><span class="brand-name">BRQMOLVEX</span></div>
  <div class="web">keystonepulsescanworks.example</div>
</section>

<!-- envelopes -->
<section class="piece envelope" style="left:29px;top:290px;height:220px">
  <svg width="522" height="80" style="position:absolute;top:0;left:0" aria-hidden="true">
    <path d="M0 0 H522 L522 20 L261 78 L0 20 Z" fill="#111214"/>
    <path d="M0 20 L261 78 L522 20" fill="none" stroke="#6cc04a" stroke-width="3"/>
  </svg>
  <div class="brand" style="position:absolute;left:200px;top:26px"><span class="brand-mark"></span><span class="brand-name" style="font-size:12px">BRQMOLVEX</span></div>
  <div class="env-window" style="left:290px;top:130px"></div>
</section>

<section class="piece envelope" style="left:29px;top:528px;height:120px">
  <div class="env-head"><div class="brand"><span class="brand-mark"></span><span class="brand-name">BRQMOLVEX</span></div></div>
  <div class="env-window" style="left:290px;top:66px"></div>
</section>

<section class="piece envelope" style="left:29px;top:660px;height:196px">
  <div class="env-return" style="top:14px">517 Thornbury Lane #2614<br>Millbrook Twp. PA. 15832<br>Phone (555) 010-2468<br>keystonepulsescanworks.example</div>
  <svg width="522" height="110" style="position:absolute;left:0;bottom:0" aria-hidden="true">
    <path d="M0 110 L0 20 L200 90 L322 90 L522 20 L522 110 Z" fill="#111214"/>
    <path d="M0 20 L200 90 L322 90 L522 20" fill="none" stroke="#6cc04a" stroke-width="3"/>
  </svg>
  <div role="img" aria-label="Soft blue and green glow decoration" style="position:absolute;left:196px;top:36px;width:130px;height:130px;border-radius:50%;background:radial-gradient(circle,rgba(58,160,232,.8),rgba(108,192,74,.35) 50%,transparent 72%)"></div>
  <div class="brand" style="position:absolute;left:50%;bottom:4px;transform:translateX(-50%);z-index:2"><span class="brand-mark"></span><span class="brand-name" style="font-size:11px">BRQMOLVEX</span></div>
</section>

<!-- letterhead -->
<section class="piece letterhead" style="left:576px;top:14px">
  <header class="lh-band">
    <div class="brand"><span class="brand-mark"></span><span class="brand-name">BRQMOLVEX</span></div>
    <div class="lh-address">517 Thornbury Lane #2614<br>Millbrook Twp. PA. 15832<br>Phone (555) 010-2468<br>nora@keystonepulsescanworks.example<br>keystonepulsescanworks.example</div>
  </header>
  <div class="lh-body">
    <p>Dear All,</p>
    <p>Thank you for choosing our mobile ultrasound team. We bring clear, careful imaging to clinics, homes and care centers across the region, with trained staff and portable equipment ready on short notice.</p>
    <p>Our technologists work closely with referring physicians to schedule studies, share results promptly and keep every patient comfortable. Reports are reviewed by board certified readers and delivered securely within one business day.</p>
    <p>We would welcome the chance to discuss how our services can support your practice. Please reach out with any questions about scheduling, coverage areas or billing.</p>
    <p>We look forward to working with you.</p>
    <p style="margin-top:150px">Regards</p>
    <div class="signature"></div>
    <p>Nora K. Pellway Hussel</p>
  </div>
</section>

<!-- second letterhead, partly covered -->
<section class="piece letterhead" style="left:722px;top:330px;width:466px;height:220px">
  <header class="lh-band" style="height:90px">
    <div class="brand" style="top:34px"><span class="brand-mark"></span><span class="brand-name">BRQMOLVEX</span></div>
    <div class="lh-address" style="top:24px">517 Thornbury Lane #2614<br>Millbrook Twp. PA. 15832<br>Phone (555) 010-2468<br>keystonepulsescanworks.example</div>
  </header>
</section>

<!-- fax cover -->
<section class="piece fax" style="left:722px;top:530px">
  <header class="fax-head">
    <div class="brand"><span class="brand-mark"></span><span class="brand-name">BRQMOLVEX</span></div>
    <div class="lh-address">517 Thornbury Lane #2614<br>Millbrook Twp. PA. 15832<br>Phone (555) 010-2468<br>keystonepulsescanworks.example</div>
  </header>
  <div class="fax-title">FAX</div>
  <div class="fax-fields">
    <span>To:</span><span>From:</span>
    <span>Phone:</span><span>Pages:</span>
    <span>Fax:</span><span>Date:</span>
    <span>Subject:</span><span>CC:</span>
  </div>
  <div class="fax-checks">
    <span>Urgent</span><span>For Review</span><span>Please Comment</span><span>Please Reply</span><span>Please Recycle</span>
  </div>
  <div class="fax-comments">Comments:</div>
</section>

</body>
</html>
```